Etikett für 100ml BIO Saunaaufguss
Zielgruppe
Wir vertreiben unter der Marke Moorhauch edle und hochpreisige Saunadüfte aus natürlichen ätherischen Ölen aus ökologischem Anbau.
Wir benötigen ein Etikett für unsere 100ml Glasflasche. Diese ist dunkelblau - nahezu schwarz.
Dies ist der Link zu der Flasche:
https://www.kelvaflakon.com/dropper-bottle-tamvo-100-ml-kelva-din18-thread/TK482207-915
Wir haben eine PDF mit Bildern anderer Hersteller angehängt.
Bitte beachten Sie die Etikettendaten PDF-Datei. Hier sind alle Daten die auf die Flasche aufgebracht werden müssen festgelegt.
Aufgabenstellung
Beachten Sie bitte die Hinweise in der Etikettendaten PDF-Datei

```html
<!DOCTYPE html>
<html lang="de">
<head>
<meta charset="utf-8">
<title>Moorhauch – Heideferne Saunaaufguss Etikett</title>
<link rel="stylesheet" href="https://fonts.googleapis.com/css2?family=Open+Sans:wght@400;600;700&display=swap">
<style>
  :root {
    --gold-light: #f3cf3c;
    --gold-dark: #c9981a;
    --paper: #ffffff;
    --ink: #1a1a1a;
    --danger: #ff0000;
    --hazard-red: #e2231a;
    --accent-blue: #2f7fc1;
    --title-gold-a: #8a5a12;
    --title-gold-b: #c89a2a;
    --leaf-green: #1f9a48;
    --logo-ink: #4c5f4a;
    --rule: #222;
  }
  * { box-sizing: border-box; margin: 0; padding: 0; }
  html, body { width: 1200px; height: 772px; overflow: hidden; background: var(--paper); }
  body { font-family: "Open Sans", Arial, sans-serif; color: var(--ink); }

  .label {
    position: relative;
    width: 1200px; height: 772px;
    background: linear-gradient(90deg, var(--gold-dark), var(--gold-light) 30%, var(--gold-light) 70%, var(--gold-dark));
  }
  .label__sheet {
    position: absolute; left: 22px; top: 19px; right: 26px; bottom: 26px;
    background: var(--paper);
  }

  /* Brand */
  .brand { position: absolute; left: 0; right: 0; top: 34px; text-align: center; }
  .brand__name { font-size: 30px; font-weight: 400; letter-spacing: 1px; color: var(--logo-ink); line-height: 1; }
  .brand__tagline { margin-top: 8px; font-size: 7px; letter-spacing: 3px; color: var(--logo-ink); }

  /* Column rules */
  .rule { position: absolute; top: 123px; width: 2px; height: 524px; background: var(--rule); }
  .rule--left { left: 302px; }
  .rule--right { left: 814px; }

  /* Left: safety */
  .safety { position: absolute; left: 21px; top: 111px; width: 272px; }
  .signal {
    width: 266px; height: 38px; background: var(--danger);
    border: 2px solid #3a6fb5; font-size: 19px; padding: 4px 6px; line-height: 1.4;
  }
  .pictograms { display: flex; gap: 6px; margin-top: 3px; margin-left: 0; }
  .pictogram { width: 64px; height: 64px; }
  .safety__text { margin-top: 10px; font-size: 13px; line-height: 24.4px; }
  .safety__text strong { font-size: 17.5px; font-weight: 700; }
  .ufi { position: absolute; left: 22px; top: 615px; font-size: 14px; }

  /* Center: product */
  .product { position: absolute; left: 285px; width: 512px; top: 116px; text-align: center; }
  .product__name, .product__kind {
    font-weight: 600;
    background: linear-gradient(180deg, var(--title-gold-b), var(--title-gold-a));
    -webkit-background-clip: text; background-clip: text; color: transparent;
  }
  .product__name { font-size: 41px; letter-spacing: 0.5px; line-height: 1.2; }
  .product__kind { font-size: 25px; line-height: 1.2; margin-top: 2px; }
  .product__art {
    position: absolute; left: 428px; top: 210px; width: 230px; height: 390px;
    border-radius: 50%;
    background: radial-gradient(circle at 50% 45%, rgba(31,154,72,0.35), rgba(31,154,72,0.12) 60%, rgba(31,154,72,0));
  }
  .volume { position: absolute; left: 660px; top: 572px; font-size: 27px; font-weight: 700; }

  /* Right: info */
  .info { position: absolute; left: 838px; top: 111px; width: 284px; font-size: 13px; line-height: 24.4px; }
  .info__title { color: var(--accent-blue); font-size: 15px; font-weight: 600; margin-bottom: 6px; }
  .info__heading { font-size: 18px; font-weight: 700; line-height: 26px; }
  .info__section { color: var(--accent-blue); font-size: 18px; font-weight: 600; line-height: 28px; margin-top: 4px; }
  .info p { margin-bottom: 2px; }
  .info .company { font-weight: 700; }
</style>
</head>
<body>
<div class="label">
  <div class="label__sheet">

    <header class="brand">
      <div class="brand__name">MOORHAUCH</div>
      <div class="brand__tagline">DÜFTE DER NATUR</div>
    </header>

    <div class="rule rule--left"></div>
    <div class="rule rule--right"></div>

    <section class="safety">
      <div class="signal">Gefahr</div>
      <div class="pictograms">
        <svg class="pictogram" viewBox="0 0 60 60" role="img" aria-label="Ausrufezeichen">
          <rect x="12" y="12" width="36" height="36" transform="rotate(45 30 30)" fill="#fff" stroke="var(--hazard-red)" stroke-width="4"/>
          <rect x="27" y="16" width="6" height="19" fill="#000"/>
          <rect x="27" y="39" width="6" height="6" fill="#000"/>
        </svg>
        <svg class="pictogram" viewBox="0 0 60 60" role="img" aria-label="Gefahrensymbol Umwelt">
          <rect x="12" y="12" width="36" height="36" transform="rotate(45 30 30)" fill="#fff" stroke="var(--hazard-red)" stroke-width="4"/>
          <rect x="20" y="24" width="20" height="14" fill="#555" opacity="0.6"/>
        </svg>
        <svg class="pictogram" viewBox="0 0 60 60" role="img" aria-label="Gefahrensymbol Gesundheit">
          <rect x="12" y="12" width="36" height="36" transform="rotate(45 30 30)" fill="#fff" stroke="var(--hazard-red)" stroke-width="4"/>
          <rect x="22" y="18" width="16" height="24" fill="#555" opacity="0.6"/>
        </svg>
        <svg class="pictogram" viewBox="0 0 60 60" role="img" aria-label="Gefahrensymbol Flamme">
          <rect x="12" y="12" width="36" height="36" transform="rotate(45 30 30)" fill="#fff" stroke="var(--hazard-red)" stroke-width="4"/>
          <rect x="22" y="20" width="16" height="22" fill="#555" opacity="0.6"/>
        </svg>
      </div>
      <p class="safety__text"><strong>Sicherheitshinweise:</strong> Flüssigkeit und Dampf leicht entzündbar. Kann allergische Hautreaktionen verursachen. Darf nicht in die Hände von Kindern gelangen. Von Hitze, heißen Oberflächen, Funken, offenen Flammen und anderen Zündquellen fernhalten. Nicht rauchen. Behälter fest verschlussen halten. Schutzhandschuhe und Augenschutz / Gesichtsschutz tragen. Bei Hautreizung oder -ausschlag: Ärztlichen Rat einholen / ärztliche Hilfe hinzuziehen. Entsorgung des Inhalts gemäß den regionalen Vorschriften. Enthält Limonene, Linalool und Geraniol als natürliche Bestandteile der ätherischen Öle.</p>
    </section>
    <div class="ufi">UFI: XXXX-XXXX-XXXXXXXX</div>

    <section class="product">
      <div class="product__name">HEIDEFERNE</div>
      <div class="product__kind">SAUNAAUFGUSS</div>
    </section>
    <div class="product__art" role="img" aria-label="Grüne Pflanzenillustration mit Eukalyptuszweigen in einem Kreis"></div>
    <div class="volume">100 ml</div>

    <section class="info">
      <div class="info__title">Warnhinweise und Beschreibung</div>
      <div class="info__heading">Inhaltsstoffe:</div>
      <p>BIO Alkohol, 100% naturreine ätherische BIO Öle von Eukalyptus, Zirbe, Minze und Grapefruit, Wasser.</p>
      <div class="info__heading">Anwendung:</div>
      <p>Etwa 4 – 5 Verschlusskappen des Konzentrats mit einem Liter Wasser vermischen und auf die heißen Steine gießen. Niemals unverdünnt anwenden!</p>
      <div class="info__section">Codedaten</div>
      <p>EAN-13 Code: 4270008815527<br>QR-Code-Link: www.moorhauch.de/qr/58203</p>
      <div class="info__section">Adressdaten</div>
      <p><span class="company">4KL GmbH</span><br>Lindenhof-Str. 12<br>48317 Hasselbrück<br><strong>Email:</strong> info@moorhauch.de<br><strong>Telefon:</strong> +49 (0)5300 / 481 2260<br><strong>Internet:</strong> www.moorhauch.de</p>
    </section>

  </div>
</div>
</body>
</html>
```